Tallwood Ridge firewood

It a new firewood outlet in Jindabyne nsw that will only sell top hardwood firewood (ironbark , red gum, grey gum, an box mix. I would like to see a web page the we can do order online payment for delivery. It will all so need to have photos of the firewood. I all so have logo for tallwood ridge firewood
Must have a modem look but easy to use I would like to see a black back ground of some sort.

Here are some other firewood web pages for ideas and firewood info
http://www.kestrelburnfuel.com.au
http://www.brindlefirewood.com.au
http://www.coppertonfirewood.com.au
http://www.wattleyhearthlogs.com.au/firewood

```html
<!DOCTYPE html>
<html lang="en">
<head>
<meta charset="utf-8">
<title>Tallwood Ridge Firewood</title>
<link rel="stylesheet" href="https://fonts.googleapis.com/css2?family=Open+Sans:wght@400;700&display=swap">
<style>
  :root {
    --page-bg: #151210;
    --logo-bg: #cbbdae;
    --frame: #5e534c;
    --nav-bg: #768ca0;
    --nav-text: #f3f5f7;
    --heading: #b9d2ea;
    --body-text: #ece6e0;
    --lead-text: #ffffff;
    --phone-text: #1a72b9;
    --phone-bg: rgba(230, 222, 214, 0.75);
    --brand-ink: #3a4f9a;
  }
  * { box-sizing: border-box; margin: 0; padding: 0; }
  html, body {
    width: 1200px; height: 691px; overflow: hidden;
    background: var(--page-bg);
    font-family: "Open Sans", sans-serif;
  }
  .site { position: relative; width: 1200px; height: 691px; }

  .brand {
    position: absolute; left: 109px; top: 0; width: 242px; height: 211px;
    background: var(--logo-bg);
    border: 1px solid var(--frame); border-top: none;
    display: flex; flex-direction: column; align-items: center; justify-content: center; gap: 14px;
  }
  .brand-mark {
    width: 54px; height: 54px; border-radius: 50%;
    background: var(--brand-ink);
  }
  .brand-name {
    font-size: 17px; font-weight: 700; color: var(--brand-ink);
    text-align: center; line-height: 1.2;
  }

  .hero {
    position: absolute; left: 370px; top: 0; width: 722px; height: 211px;
    border: 1px solid var(--frame); border-top: none;
    background: linear-gradient(135deg, #a57a4f 0%, #d9b47f 35%, #8c5f3d 60%, #c79a66 80%, #6e4a30 100%);
  }
  .hero-phone {
    position: absolute; right: 14px; top: 129px;
    padding: 0 5px; height: 42px; line-height: 42px;
    background: var(--phone-bg);
    color: var(--phone-text);
    font-size: 32px; font-weight: 700;
  }

  .site-nav {
    position: absolute; left: 109px; top: 235px; width: 240px; height: 186px;
    background: var(--nav-bg);
    padding: 16px 16px 0 0;
    text-align: right;
  }
  .site-nav ul { list-style: none; }
  .site-nav li { font-size: 15px; line-height: 21.8px; }
  .site-nav a { color: var(--nav-text); text-decoration: none; }
  .site-nav .current a { font-weight: 700; color: #ffffff; }

  .content {
    position: absolute; left: 371px; top: 234px; width: 722px;
    color: var(--body-text);
    font-size: 15px; line-height: 21.8px;
  }
  .content h1 {
    font-size: 26px; font-weight: 700; color: var(--heading);
    line-height: 36px; margin-bottom: 11px;
  }
  .content .lead { font-weight: 700; color: var(--lead-text); margin-bottom: 21px; }
  .content p + p { margin-top: 21px; }
</style>
</head>
<body>
<div class="site">
  <header>
    <div class="brand">
      <div class="brand-mark"></div>
      <div class="brand-name">Tallwood Ridge Firewood</div>
    </div>
    <div class="hero" role="img" aria-label="Photograph of a stacked pile of split hardwood firewood logs">
      <div class="hero-phone">026 45 118 302</div>
    </div>
  </header>

  <nav class="site-nav">
    <ul>
      <li class="current"><a href="#">Home</a></li>
      <li><a href="#">Products</a></li>
      <li><a href="#">Order</a></li>
      <li><a href="#">About Us</a></li>
      <li><a href="#">Contact Us</a></li>
      <li><a href="#">Page Title</a></li>
      <li><a href="#">Another Page</a></li>
    </ul>
  </nav>

  <main class="content">
    <h1>Welcome to Tallwood Ridge Firewood</h1>
    <p class="lead">Jindabyne's new firewood outlet sells only top hardwood: ironbark, red gum, grey gum and a seasoned box mix. Every load is split to size and dried so it lights easily, burns hot and lasts all night long. Choose your wood, pay securely online and we will deliver it straight to your door.</p>
    <p>Ironbark is dense and slow burning, ideal for long cold nights in the Snowy Mountains. Red gum gives a strong, steady heat with a beautiful glowing bed of coals. Grey gum lights quickly and burns clean, while our box mix offers great value for everyday heating. All of our firewood is sourced responsibly and checked for moisture before it leaves the yard.</p>
    <p>Ordering is simple. Pick a wood type and load size on the Order page, enter your delivery address and pay online by card. We deliver across Jindabyne and the surrounding high country, and we will call ahead to confirm a time that suits you. Pickup from our yard is also available.</p>
  </main>
</div>
</body>
</html>
```